Cell Tower company needs website updated

We need a website that does not look like it was designed in the early 1990's. The company fabricates, installs and reinforces communication towers throughout the US, Caribbean, Central and S. America. We are located in Pensacola Florida. Our tower technicians travel to wherever the work is. I have some good pictures taken from towers to use on the site. I want the site to reflect the excitement that the wireless communication industry has. I want to the company to look exciting and attract new employees. The majority of our business is modifying and reinforcing existing cell towers to accept all the new tower top antennas that the increasing wireless mobile world demands.

I have added some sample photos from our business to our ArtFoundry profile.

We are now going through each design to find what is most suitable for our needs. Thank you all for your time in this matter.

Wireless Communication

```html
<!DOCTYPE html>
<html lang="en">
<head>
<meta charset="utf-8">
<title>SkyMast Structures, Inc.</title>
<link rel="stylesheet" href="https://fonts.googleapis.com/css2?family=Arimo:wght@400;700&family=Roboto+Condensed:wght@400;700&display=swap">
<style>
:root{
  --ink:#555;
  --title:#666;
  --red:#c8102e;
  --nav-bg:#232323;
  --nav-line:#3a3a3a;
  --side-bg:#f4efef;
  --green:#6e9a12;
  --footer-bg:#222;
  --footer-text:#8a8a8a;
  --footer-head:#d6d6d6;
  --white:#fff;
  --storm-dark:#2f3133;
  --storm-mid:#6a6c6e;
  --storm-light:#a9abad;
  --sky-blue:#b7cbd9;
}
*{box-sizing:border-box;margin:0;padding:0}
html,body{width:1200px;height:1173px;overflow:hidden;background:var(--white);font-family:"Arimo",Arial,sans-serif}
.page{position:relative;width:1200px;height:1173px}
.hero{position:absolute;left:0;top:0;width:1200px;height:497px;
  background:
    radial-gradient(ellipse 380px 160px at 620px 90px,rgba(40,42,44,.85),rgba(40,42,44,0)),
    radial-gradient(ellipse 320px 140px at 980px 130px,rgba(150,152,154,.7),rgba(150,152,154,0)),
    radial-gradient(ellipse 300px 150px at 180px 200px,rgba(125,128,130,.75),rgba(125,128,130,0)),
    radial-gradient(ellipse 420px 180px at 760px 300px,rgba(92,94,96,.8),rgba(92,94,96,0)),
    radial-gradient(ellipse 300px 160px at 1130px 420px,rgba(183,203,217,.95),rgba(183,203,217,0)),
    radial-gradient(ellipse 360px 140px at 90px 430px,rgba(170,178,172,.8),rgba(170,178,172,0)),
    linear-gradient(180deg,var(--storm-dark) 0%,var(--storm-mid) 45%,var(--storm-light) 85%,var(--sky-blue) 100%)}
.sidebar{position:absolute;left:192px;top:136px;width:206px}
.brand{height:102px;background:var(--white);display:flex;align-items:center;justify-content:center;gap:8px}
.brand-mark{width:14px;height:14px;border-radius:50%;background:var(--red)}
.brand-name{font-size:21px;color:#222}
.nav{background:var(--nav-bg);padding:2px 0 6px}
.nav a{display:flex;justify-content:space-between;align-items:center;margin:0 24px;height:28.4px;
  border-bottom:1px solid var(--nav-line);color:#cfcfcf;font-size:10.5px;text-decoration:none}
.nav a:last-child{border-bottom:none}
.nav a.active{color:var(--white);margin-right:25px}
.nav a.active span.arrow{width:32px;height:30px;background:var(--red);color:#fff;display:flex;align-items:center;justify-content:center;font-size:11px}
.side-panel{position:absolute;left:192px;top:547px;width:206px;height:413px;background:var(--side-bg);padding:13px 12px}
.jobs{display:flex;align-items:center;height:49px;background:var(--green);color:#fff;font-size:10px;font-weight:700;line-height:1.35}
.jobs .doc{width:22px;height:26px;background:#f2f2f2;margin:0 14px 0 16px;transform:rotate(-12deg)}
.jobs .label{flex:1}
.jobs .go{width:40px;height:100%;border-left:1px solid #88b131;display:flex;align-items:center;justify-content:center;font-size:18px}
.partner{margin-top:25px;height:62px;background:var(--white);border:1px solid #e2dcdc;display:flex;align-items:center;gap:12px;padding:0 8px}
.partner .seal{width:50px;height:50px;border-radius:50%;background:#e9ece4;border:3px solid #2d5a32}
.partner .name{font-family:Georgia,serif;font-size:13px;color:#b7a57a;line-height:1.3}
.content{position:absolute;left:434px;top:533px;width:570px}
.content h1{font-size:21px;font-weight:400;color:var(--title)}
.content .tagline{font-size:12px;color:var(--red);margin-left:96px;margin-top:1px;padding-bottom:8px;border-bottom:1px dashed #ddd}
.content p{font-size:11px;line-height:1.3;color:var(--ink)}
.intro{margin-top:30px}
.photos{display:flex;justify-content:space-between;margin:22px 0 26px}
.photo{width:271px;height:153px;border-radius:3px}
.photo.masts{background:linear-gradient(160deg,#3b72c4,#6b9ee0)}
.photo.climber{width:274px;background:linear-gradient(160deg,#4f8ed6,#b7d5ef)}
.footer{position:absolute;left:0;top:960px;width:1200px;height:213px;background:var(--footer-bg)}
.f-brand{position:absolute;left:194px;top:57px;color:#ddd;font-size:21px}
.f-copy{position:absolute;left:194px;top:102px;font-size:8px;color:var(--footer-text)}
.f-col h3{font-family:"Roboto Condensed",sans-serif;font-size:12px;letter-spacing:1px;color:var(--footer-head);font-weight:700}
.f-contact{position:absolute;left:435px;top:44px}
.f-contact .org{font-family:"Roboto Condensed",sans-serif;font-size:12px;color:var(--footer-text);margin:14px 0 12px}
.f-contact li{list-style:none;display:flex;align-items:center;gap:13px;height:18px;font-size:8.5px;font-weight:700;color:var(--footer-text)}
.f-contact svg{width:11px;height:11px;fill:#8a8a8a}
.f-social{position:absolute;left:663px;top:44px}
.f-social .icons{display:flex;gap:4px;margin-top:16px}
.f-social .icons span{width:23px;height:23px;border-radius:50%;background:#aaa}
.f-social .icons span:first-child{background:#3a78c3}
</style>
</head>
<body>
<div class="page">
  <div class="hero" role="img" aria-label="Red and white steel communication towers with antennas and guy wires rising into a dramatic stormy sky"></div>

  <aside class="sidebar">
    <div class="brand"><span class="brand-mark"></span><span class="brand-name">SkyMast</span></div>
    <nav class="nav">
      <a class="active" href="#">Home<span class="arrow">›</span></a>
      <a href="#">Tower Reinforcement</a>
      <a href="#">Rapid Deployment Site</a>
      <a href="#">Towers</a>
      <a href="#">Monopole Reinforcement</a>
      <a href="#">Tower Accessories</a>
      <a href="#">Custom Steel Fabrication</a>
      <a href="#">Antenna Support Structure</a>
      <a href="#">Construction Services</a>
      <a href="#">Contact Us</a>
    </nav>
  </aside>

  <div class="side-panel">
    <a class="jobs"><span class="doc"></span><span class="label">EMPLOYMENT<br>OPPORTUNITIES</span><span class="go">›</span></a>
    <div class="partner"><span class="seal"></span><span class="name">Guild of<br>Tower Riggers</span></div>
  </div>

  <main class="content">
    <h1>SkyMast Structures, Inc.</h1>
    <div class="tagline">Towering above the rest</div>
    <p class="intro">SkyMast Structures, Inc., is an experienced and innovative provider of communication towers, tower reinforcements and related support services. Specializing in the manufacturing, installation, and maintenance of communication infrastructure products, we are regarded as pioneers in the communications industry. From the innovative structural design ideas we develop for antenna systems and tower reinforcements, to the alternative tower installation techniques we offer, SkyMast consistently delivers high quality solutions for the commercial, defense, federal, and international markets..</p>
    <div class="photos">
      <div class="photo masts" role="img" aria-label="Two lattice towers seen from below against a blue sky"></div>
      <div class="photo climber" role="img" aria-label="Technician climbing a steel lattice tower under a cloudy blue sky"></div>
    </div>
    <p>We invite you to explore our website, then contact us; so that we may begin to develop and implement the superior, cost effective, and timely solutions that your individual project requires.</p>
  </main>

  <footer class="footer">
    <div class="f-brand">SkyMast</div>
    <div class="f-copy">Copyright © 2014 SkyMast Structures.</div>
    <div class="f-col f-contact">
      <h3>CONTACT INFO</h3>
      <div class="org">SkyMast Structures Incorporated</div>
      <ul>
        <li><svg viewBox="0 0 12 12"><path d="M6 0a4 4 0 0 0-4 4c0 3 4 8 4 8s4-5 4-8a4 4 0 0 0-4-4zm0 5.5A1.5 1.5 0 1 1 6 2.5a1.5 1.5 0 0 1 0 3z"/></svg>#48 Harbor Road, Bayview State 5521</li>
        <li><svg viewBox="0 0 12 12"><path d="M2 0l2 0 1 3-1.5 1a7 7 0 0 0 4.5 4.5L9 7l3 1v2a2 2 0 0 1-2 2A10 10 0 0 1 0 2a2 2 0 0 1 2-2z"/></svg>555 210 48831</li>
        <li><svg viewBox="0 0 12 12"><path d="M3 0h6v3H3zM0 4h12v5h-2v3H2V9H0zm3 3v4h6V7z"/></svg>555 210 48831</li>
        <li><svg viewBox="0 0 12 12"><path d="M0 2h12v8H0zm1 1l5 4 5-4"/></svg>hello@skymast-towers.test</li>
        <li><svg viewBox="0 0 12 12"><circle cx="6" cy="6" r="5.5" fill="none" stroke="#8a8a8a"/><path d="M0.5 6h11M6 .5v11" stroke="#8a8a8a"/></svg>www.skymast-towers.test</li>
      </ul>
    </div>
    <div class="f-col f-social">
      <h3>SOCIAL LINKS</h3>
      <div class="icons"><span></span><span></span><span></span><span></span></div>
    </div>
  </footer>
</div>
</body>
</html>
```